Classic Personal Business Card in Regatta Dane Whitcomb Style (Horizontal - Raised Ink)

If you ever seen a Dane Whitcomb Regatta shirt, you will know that the signature of that shirt is small monogrammed icon on the left pocket. I envision my personal business card using some of these elements. I am in the oil exploration industry, which is very conservative and I want a card that looks great but still reflects that classic conservatism. I specifically do land management work, which means I determine who owns mineral rights, I lease those rights for larger companies to then drill for crude oil and natural gas

1. I have designed a small logo (which definitely could use some help) that I would like to be pretty small, centered in the middle of the card, and near the top of the card (color - navy blue or similar) Please feel free to make this logo infinitely better. However, I am not looking for anything abstract/

2. I want my name and designation (Morgan D. Hartwell, RPL) centered in the middle of the card. As far as font, I'm looking for a classic, strong (almost masculine) cursive font (I realize masculine + cursive is a little oxymoronic) and I would like it to the color to be Gold.

3. I would like my name (see above) to sit on top of a thin, centered navy blue (or similar) line as if it were almost a signature on a line. I want the lower-case letters that normally would dip below the line (which is y and p in my case) to do the same. I'll attach an example to help illustrate what I mean.

4. The rest of the card is my contact information. Because I am shoot for a more centered and balance look, I would like the placement of my contact information to also be centered and balance. Font should be a very classic, professional font. My first inclination is to use black for the color but I'm open to other suggestions.

Contact information:

Phone: (555) 014-2387
Email: mdhartwl@qovantri.com

Important Note: My hope is to have these printed with Raised Ink on High Quality High Quality Card Stock so it must conform to this Necessity.

Project Deadline Extended Reason: I am having major internet trouble. So I am not able to look at the submissions and provide feedback in a timely fashion. Also, it is difficult to access the site from just my phone. Added Saturday, November 22, 2014

Target Market(s)

US Oil Executives

Industry/Entity Type

Conservative

Contact Information for Business Card

I've posted a new logo that needs some clean up and a new idea for the top and bottom border of the card. I would like the logo to be centered in the top border with a white barrier on either side between the logo and the border. I've also posted color codes below.

Thanks

Requirements
Must have
• Color Codes:
• Blue: R - 0 G - 0 B - 102
• Gold R - 102 G - 102 B - 0

```html
<!DOCTYPE html>
<html lang="en">
<head>
<meta charset="utf-8">
<title>Morgan D. Hartwell, RPL – Business Card</title>
<link rel="stylesheet" href="https://fonts.googleapis.com/css2?family=Kalam:wght@400&family=Arimo:wght@400&display=swap">
<style>
  :root {
    --backdrop: #e9e6e1;
    --card-top: #fbfbfb;
    --card-bottom: #e4e4e4;
    --navy: rgb(0, 0, 102);
    --gold: rgb(102, 102, 0);
    --contact: #3a3a3a;
  }
  html, body {
    margin: 0;
    width: 1200px;
    height: 852px;
    overflow: hidden;
    background: var(--backdrop);
  }
  .card {
    position: absolute;
    left: 100px;
    top: 116px;
    width: 1000px;
    height: 620px;
    background: radial-gradient(ellipse at 50% 35%, var(--card-top) 0%, var(--card-bottom) 100%);
    box-shadow: 0 6px 24px rgba(0,0,0,0.18);
    text-align: center;
  }
  .brand {
    position: absolute;
    top: 70px;
    left: 0;
    right: 0;
    display: flex;
    align-items: center;
    justify-content: center;
    gap: 14px;
    font-family: "Arimo", Arial, sans-serif;
    font-size: 22px;
    color: var(--navy);
    letter-spacing: 0.06em;
  }
  .brand-dot {
    width: 22px;
    height: 22px;
    border: 3px solid var(--navy);
    border-radius: 50%;
  }
  .signature {
    position: absolute;
    top: 238px;
    left: 0;
    right: 0;
  }
  .signature-name {
    margin: 0;
    font-family: "Kalam", cursive;
    font-weight: 400;
    font-size: 66px;
    line-height: 1;
    color: var(--gold);
    letter-spacing: 0.02em;
  }
  .signature-line {
    display: block;
    margin: -14px auto 0;
    width: 680px;
    height: 3px;
    background: var(--navy);
  }
  .contact {
    position: absolute;
    top: 390px;
    left: 0;
    right: 0;
    margin: 0;
    font-family: "Arimo", Arial, sans-serif;
    font-size: 25px;
    line-height: 52px;
    color: var(--contact);
    font-style: normal;
  }
</style>
</head>
<body>
  <section class="card">
    <div class="brand">
      <span class="brand-dot"></span>
      <span class="brand-name">Hartwell Land</span>
    </div>
    <div class="signature">
      <h1 class="signature-name">Morgan D. Hartwell, RPL</h1>
      <span class="signature-line"></span>
    </div>
    <address class="contact">
      <div class="contact-phone">Phone no.: (555) 014-2387</div>
      <div class="contact-email">E-mail ad.: mdhartwl@qovantri.com</div>
    </address>
  </section>
</body>
</html>
```